Website R86 coffee

I am opening a small business selling locally roasted coffee online. To start with I want a site with three pages. 1. A welcome page with logo and mission/vision. 2. Shopping/ordering page. 3. About Us page. The brand is "R86 Coffee - A warm start to every day". We are giving back to the downs syndrome community by employing people with down syndrome (Trisomy 21) and buy donating to down syndrome research.

Target Market(s)

Families and friends of people with downs syndrome

Coding

Coded - Design and coding required

Number of Pages Required

3 page

```html
<!DOCTYPE html>
<html lang="en">
<head>
<meta charset="utf-8">
<title>R86 Coffee - A warm start to every day</title>
<link href="https://fonts.googleapis.com/css2?family=Mulish:wght@400;500;600&family=Roboto+Condensed:wght@400&display=swap" rel="stylesheet">
<style>
:root{
  --ink:#1d1d1d;
  --text:#3a3a3a;
  --accent:#a8825e;
  --line:#c9ab8c;
  --card:#f4f4f4;
  --white:#ffffff;
  --hero-a:#5a4434;
  --hero-b:#2e2119;
  --band:#2a2521;
  --footer:#efe6da;
}
*{margin:0;padding:0;box-sizing:border-box}
html,body{width:1200px;height:3467px;overflow:hidden}
body{position:relative;background:var(--white);font-family:"Mulish",sans-serif;color:var(--text)}
.abs{position:absolute}
a{color:inherit;text-decoration:none}

/* header */
.site-header{left:0;top:0;width:1200px;height:94px;background:var(--white)}
.brand-box{border:2px solid var(--ink);display:flex;flex-direction:column;justify-content:center;align-items:center}
.brand-name{font-size:38px;font-weight:400;color:var(--ink);letter-spacing:1px;line-height:1}
.brand-tag{font-size:8px;font-weight:600;color:var(--ink);letter-spacing:1.5px;text-transform:uppercase;margin-top:4px}
.nav a{position:absolute;top:42px;font-size:13px;color:var(--ink);white-space:nowrap}
.nav .active{font-weight:600;border-bottom:1px solid var(--ink);padding-bottom:4px}
.cart-icon{width:26px;height:26px;background:var(--accent);top:38px;left:920px}

/* hero */
.hero{left:0;top:94px;width:1200px;height:494px;background:radial-gradient(ellipse at 35% 30%,#9b8777 0%,var(--hero-a) 45%,var(--hero-b) 100%)}
.hero-title{left:0;width:1200px;top:278px;text-align:center;font-family:"Roboto Condensed",sans-serif;font-size:41px;line-height:46px;color:var(--white)}
.btn-outline{left:550px;top:383px;width:98px;height:30px;border:1px solid var(--accent);color:var(--accent);font-size:15px;display:flex;align-items:center;justify-content:center;background:rgba(0,0,0,.25)}

/* welcome */
.cup-photo{left:195px;top:673px;width:242px;height:242px;border-radius:50%;background:radial-gradient(circle at 50% 50%,#c9a987 0%,#eeeae6 35%,#fafafa 70%,#f0f0f0 100%);box-shadow:0 8px 18px rgba(0,0,0,.12)}
.leaf-deco{left:0;top:800px;width:300px;height:270px;background:radial-gradient(ellipse at 30% 50%,rgba(220,200,180,.35),rgba(255,255,255,0) 70%)}
.bean-deco{left:720px;top:590px;width:480px;height:200px;background:radial-gradient(ellipse at 70% 50%,rgba(215,215,215,.35),rgba(255,255,255,0) 70%)}
.h2{font-size:36px;font-weight:500;color:var(--ink);line-height:1.1}
.welcome-title{left:539px;top:668px}
.body-copy{font-size:14px;line-height:25.5px;color:var(--text)}
.welcome-copy{left:539px;top:720px;width:475px}
.welcome-copy p+p{margin-top:8px}
.text-link{color:var(--accent);font-size:15px;border-bottom:1px solid var(--accent);padding-bottom:3px}

/* products */
.products-title{left:0;width:1200px;top:1054px;text-align:center}
.products-intro{left:270px;width:660px;top:1104px;text-align:center}
.product-card{width:402px;height:494px;background:var(--card)}
.product-photo{position:absolute;left:100px;top:50px;width:200px;height:290px;border-radius:10px 10px 18px 18px}
.bag-kraft{background:linear-gradient(180deg,#c8a17f 0%,#b98f6c 60%,#8f6a4a 100%)}
.bag-dark{background:linear-gradient(180deg,#c39c78 0%,#b48d6a 60%,#2a2624 61%,#1d1b1a 100%)}
.bag-white{background:linear-gradient(180deg,#f7f7f7 0%,#ececec 60%,#d9c6ae 61%,#cdb79d 100%)}
.product-name{position:absolute;left:0;width:100%;top:376px;text-align:center;font-size:16px;color:var(--ink)}
.product-desc{position:absolute;left:20px;right:20px;top:405px;text-align:center;font-size:12.5px;line-height:20px;color:var(--text)}
.product-price{position:absolute;left:20px;top:462px;font-size:15px;font-weight:600;color:var(--accent)}
.product-link{position:absolute;right:22px;top:458px;font-size:14px}

/* vision */
.vision-title{left:190px;top:2294px}
.vision-copy{left:190px;top:2346px;width:380px}
.mission-title{left:190px;top:2446px}
.mission-copy{left:190px;top:2496px;width:385px}
.photo-roast{left:596px;top:2292px;width:205px;height:362px;background:linear-gradient(180deg,#6b4b34 0%,#4a2f21 55%,#8a8f93 100%)}
.photo-child{left:807px;top:2292px;width:204px;height:362px;background:linear-gradient(180deg,#55623a 0%,#6f7a4e 45%,#3e4a6a 100%)}

/* giving band */
.giving{left:0;top:2734px;width:1200px;height:450px;background:radial-gradient(ellipse at 50% 40%,#4a3e35 0%,var(--band) 70%)}
.giving-text{left:200px;width:800px;top:2873px;text-align:center;font-size:23px;line-height:40px;color:var(--white)}
.giving-link{left:0;width:1200px;top:3020px;text-align:center}

/* footer */
.site-footer{left:0;top:3184px;width:1200px;height:283px;background:var(--footer)}
.footer-nav a{position:absolute;top:3330px;font-size:13px;color:var(--ink)}
.contact{top:3370px;font-size:13px;color:var(--ink);display:flex;align-items:center;gap:8px}
.copyright{left:191px;top:3430px;font-size:12.5px;color:var(--text)}
.social{top:3423px;width:30px;height:30px;border:1.5px solid var(--ink)}
</style>
</head>
<body>

<header class="site-header abs">
  <div class="brand-box abs" style="left:191px;top:13px;width:257px;height:74px">
    <span class="brand-name">R86 Coffee</span>
    <span class="brand-tag">A warm start to every day</span>
  </div>
  <nav class="nav">
    <a class="active" style="left:611px">Home</a>
    <a style="left:684px">Shop Our Products</a>
    <a style="left:831px">About Us</a>
    <span class="cart-icon abs">
      <svg width="26" height="26" viewBox="0 0 26 26"><path d="M6 8h2l2 8h8l2-6H9" fill="none" stroke="#fff" stroke-width="1.6"/><circle cx="11" cy="19" r="1.3" fill="#fff"/><circle cx="17" cy="19" r="1.3" fill="#fff"/></svg>
    </span>
    <a style="left:954px">Cart (0)</a>
  </nav>
</header>

<section class="hero abs" role="img" aria-label="Photo of a latte cup on a saucer beside a burlap sack spilling roasted coffee beans on a wooden table"></section>
<h1 class="hero-title abs" style="font-weight:400">We are a Boutique Coffee Roaster in<br>Australia</h1>
<a class="btn-outline abs">Shop Now</a>

<div class="bean-deco abs" role="img" aria-label="Faint sketched coffee beans decoration"></div>
<div class="leaf-deco abs" role="img" aria-label="Faint sketched coffee branch decoration"></div>
<div class="cup-photo abs" role="img" aria-label="Top view of a latte with heart latte art in a white cup"></div>

<h2 class="h2 welcome-title abs">Welcome to R86 Coffee</h2>
<div class="body-copy welcome-copy abs">
  <p>Lorem ipsum dolor sit amet, consectetuer adipiscing elit, sed diam nonummy nibh euismod tincidunt ut laoreet dolore magna aliquam erat volutpat. Ut wisi enim ad minim veniam, quis nostrud exerci tation ullamcorper suscipit lobortis nisl ut aliquip ex ea commodo consequat.</p>
  <p>Duis autem vel eum iriure dolor in hendrerit in vulputate velit esse molestie consequat, vel illum dolore eu feugiat nulla facilisis at vero eros et accumsan et iusto odio dignissim qui blandit praesent luptatum zzril delenit augue duis dolore te feugait nulla facilisi.</p>
</div>
<a class="text-link abs" style="left:540px;top:950px">Read More About Our Mission &amp; Vision</a>

<h2 class="h2 products-title abs">Our Products</h2>
<p class="body-copy products-intro abs">Lorem ipsum dolor sit amet, consectetuer adipiscing elit, sed diam nonummy nibh euismod tincidunt ut laoreet dolore magna aliquam erat volutpat ut wisi enim ad minim .</p>

<article class="product-card abs" style="left:187px;top:1184px">
  <div class="product-photo bag-kraft" role="img" aria-label="Kraft coffee bag with a sketched coffee cup illustration"></div>
  <h3 class="product-name" style="font-weight:500">Product Name 1</h3>
  <p class="product-desc">Lorem ipsum dolor sit amet, consectetuer adipiscing lorem ipsum dolor sit amet, consectetuer adipiscing</p>
  <span class="product-price">$ 12.45</span>
  <a class="text-link product-link">View Details</a>
</article>
<article class="product-card abs" style="left:609px;top:1184px">
  <div class="product-photo bag-dark" role="img" aria-label="Kraft and black coffee bag with a sketched coffee branch illustration"></div>
  <h3 class="product-name" style="font-weight:500">Product Name 2</h3>
  <p class="product-desc">Lorem ipsum dolor sit amet, consectetuer adipiscing lorem ipsum dolor sit amet, consectetuer adipiscing</p>
  <span class="product-price">$ 12.45</span>
  <a class="text-link product-link">View Details</a>
</article>
<article class="product-card abs" style="left:187px;top:1712px">
  <div class="product-photo bag-dark" role="img" aria-label="Kraft and black coffee bag with a sketched coffee branch illustration"></div>
  <h3 class="product-name" style="font-weight:500">Product Name 3</h3>
  <p class="product-desc">Lorem ipsum dolor sit amet, consectetuer adipiscing lorem ipsum dolor sit amet, consectetuer adipiscing</p>
  <span class="product-price">$ 12.45</span>
  <a class="text-link product-link">View Details</a>
</article>
<article class="product-card abs" style="left:609px;top:1712px">
  <div class="product-photo bag-white" role="img" aria-label="White and beige coffee bag with a sketched coffee cup illustration"></div>
  <h3 class="product-name" style="font-weight:500">Product Name 4</h3>
  <p class="product-desc">Lorem ipsum dolor sit amet, consectetuer adipiscing lorem ipsum dolor sit amet, consectetuer adipiscing</p>
  <span class="product-price">$ 12.45</span>
  <a class="text-link product-link">View Details</a>
</article>

<h2 class="h2 vision-title abs">Our Vision</h2>
<p class="body-copy vision-copy abs">Develop a company that markets coffee and related products to family and friends of the down syndrome community</p>
<h2 class="h2 mission-title abs">Our Mission</h2>
<p class="body-copy mission-copy abs">Create and grow an online &nbsp;company selling &nbsp;contract roasted coffee. As growth permits become a fully vertically integrated &nbsp;coffee company from roasting to our own coffee shop. The company will give significant funds to medical research &nbsp;in downs syndrome and we will hire as many people with Downs syndrome as possible.</p>
<div class="photo-roast abs" role="img" aria-label="Roasted coffee beans pouring from a roaster scoop into a steel bin"></div>
<div class="photo-child abs" role="img" aria-label="Child lying on grass beside a green football"></div>

<section class="giving abs" role="img" aria-label="Dark photo of hands holding cups of latte art coffee"></section>
<p class="giving-text abs">We are giving back to the downs syndrome community by employing people with down syndrome (Trisomy 21) and buy donating to down syndrome research.</p>
<div class="giving-link abs"><a class="text-link">Shop Now</a></div>

<footer class="site-footer abs"></footer>
<div class="brand-box abs" style="left:487px;top:3228px;width:226px;height:65px">
  <span class="brand-name" style="font-size:32px">R86 Coffee</span>
  <span class="brand-tag" style="font-size:7px">A warm start to every day</span>
</div>
<nav class="footer-nav">
  <a style="left:462px">Home</a>
  <a style="left:535px">Shop Our Products</a>
  <a style="left:683px">About Us</a>
</nav>
<div class="contact abs" style="left:410px">
  <svg width="20" height="20" viewBox="0 0 20 20"><path d="M5 2l3 3-2 2c1 3 3 5 6 6l2-2 3 3-2 3C9 17 3 11 2 4z" fill="none" stroke="#1d1d1d" stroke-width="1.2"/></svg>
  <span>Call Us: +1 (555) 014-2286</span>
</div>
<div class="contact abs" style="left:622px">
  <svg width="22" height="18" viewBox="0 0 22 18"><rect x="1.5" y="3" width="19" height="13" fill="none" stroke="#1d1d1d" stroke-width="1.2"/><path d="M1.5 3l9.5 7 9.5-7" fill="none" stroke="#1d1d1d" stroke-width="1.2"/></svg>
  <span>hello@r86coffee.com</span>
</div>
<p class="copyright abs">© 2021 R86 Coffee. All Rights Reserved.</p>
<span class="social abs" style="left:877px"></span>
<span class="social abs" style="left:912px"></span>
<span class="social abs" style="left:947px"></span>
<span class="social abs" style="left:982px"></span>

</body>
</html>
```